Chiropractic Software Company needs Business Cards

We need a bushiness card design for use at a Chiropractic conference. We build billing, practice management, and medical documentation software. Our product is Vantora Chiropractic Software(Vantora for short). On top of our software we have practice success coaches that coordinate with our chiropractor clients to help them grow their practice and treat more patients. Our logo colors are tried-and-true orange-and-blue. We'd like a sterile white background and a clean layout; organizing the following information: Name, Position/Title, Phone Number, Address, email, and our website. On the backside we'd like our Logo and our slogan, "Your Clinic Keel" and our website(http://www.vantorachiropracticsoftware.example)

Industry/Entity Type

Business

```html
<!DOCTYPE html>
<html lang="en">
<head>
<meta charset="utf-8">
<title>Vantora Chiropractic Software – Business Card</title>
<link href="https://fonts.googleapis.com/css2?family=Montserrat:wght@400;600;700&display=swap" rel="stylesheet">
<style>
  :root {
    --blue: #1f78c8;
    --blue-deep: #1456a8;
    --blue-light: #2aa3d8;
    --orange: #e8641e;
    --grey-text: #6b6b6b;
    --rule: #cfcfcf;
    --paper: #ffffff;
    --backdrop: #d9d9d9;
  }
  * { box-sizing: border-box; margin: 0; padding: 0; }
  html, body { width: 1135px; height: 1200px; overflow: hidden; }
  body {
    background: var(--backdrop);
    font-family: "Montserrat", Arial, sans-serif;
    display: flex; flex-direction: column; align-items: center; justify-content: center;
    gap: 60px;
  }
  .card {
    position: relative;
    width: 900px; height: 514px;
    background: var(--paper);
    overflow: hidden;
    box-shadow: 0 4px 14px rgba(0,0,0,.18);
  }
  .card__waves { position: absolute; inset: 0; width: 100%; height: 100%; }

  /* back side */
  .back__website {
    position: absolute; top: 22px; right: 48px;
    color: #fff; font-size: 22px; letter-spacing: .5px;
  }
  .back__brand {
    position: absolute; left: 0; right: 0; top: 190px;
    display: flex; flex-direction: column; align-items: center; gap: 18px;
  }
  .brand { display: flex; align-items: center; gap: 16px; }
  .brand__dot { width: 34px; height: 34px; border-radius: 50%; background: var(--orange); }
  .brand__name { font-weight: 700; color: var(--blue-deep); letter-spacing: 4px; }
  .back__brand .brand__name { font-size: 64px; }
  .slogan { color: var(--blue); font-size: 26px; font-weight: 600; letter-spacing: 1px; }

  /* front side */
  .front__identity { position: absolute; left: 60px; top: 110px; }
  .front__name { color: var(--blue); font-size: 40px; font-weight: 700; letter-spacing: 6px; }
  .front__position { color: var(--grey-text); font-size: 26px; letter-spacing: 5px; margin-top: 2px; }
  .front__rule {
    position: absolute; left: 60px; right: 60px; top: 198px;
    height: 2px; background: linear-gradient(90deg, var(--rule), #e8e8e8 80%, transparent);
  }
  .front__brand { position: absolute; right: 60px; top: 100px; }
  .front__brand .brand { gap: 10px; }
  .front__brand .brand__dot { width: 20px; height: 20px; }
  .front__brand .brand__name { font-size: 34px; letter-spacing: 2px; }
  .contact { position: absolute; left: 60px; top: 228px; list-style: none; }
  .contact li {
    display: flex; align-items: center; gap: 14px;
    color: var(--blue); font-size: 22px; letter-spacing: 3px; line-height: 36px;
  }
  .contact svg { width: 20px; height: 20px; flex: none; }
</style>
</head>
<body>

<section class="card card--back" aria-label="Card back">
  <svg class="card__waves" viewBox="0 0 900 514" preserveAspectRatio="none" aria-hidden="true">
    <defs>
      <linearGradient id="bandTop" x1="0" x2="1" y1="0" y2="0">
        <stop offset="0" stop-color="#1456a8"/>
        <stop offset=".5" stop-color="#2a8fd6"/>
        <stop offset="1" stop-color="#1d6fc2"/>
      </linearGradient>
    </defs>
    <path d="M0 0 H900 V88 C700 120 520 40 300 60 C180 70 80 95 0 110 Z" fill="url(#bandTop)"/>
    <path d="M0 118 C90 102 190 76 300 68 C520 50 700 128 900 98" fill="none" stroke="var(--orange)" stroke-width="9"/>
  </svg>
  <p class="back__website">www.vantorachiropracticsoftware.example</p>
  <div class="back__brand">
    <div class="brand">
      <span class="brand__dot"></span>
      <span class="brand__name">VANTORA</span>
    </div>
    <p class="slogan">“YOUR CLINIC KEEL”</p>
  </div>
</section>

<section class="card card--front" aria-label="Card front">
  <svg class="card__waves" viewBox="0 0 900 514" preserveAspectRatio="none" aria-hidden="true">
    <defs>
      <linearGradient id="bandBottom" x1="0" x2="1" y1="0" y2="0">
        <stop offset="0" stop-color="#1d6fc2"/>
        <stop offset=".5" stop-color="#2aa3d8"/>
        <stop offset="1" stop-color="#1456a8"/>
      </linearGradient>
    </defs>
    <path d="M0 410 C160 400 330 470 560 455 C720 445 820 400 900 380 V514 H0 Z" fill="url(#bandBottom)"/>
    <path d="M0 398 C160 388 330 458 560 443 C720 433 820 388 900 368" fill="none" stroke="var(--orange)" stroke-width="9"/>
  </svg>

  <div class="front__identity">
    <p class="front__name">YOUR NAME</p>
    <p class="front__position">POSITION</p>
  </div>
  <div class="front__brand">
    <div class="brand">
      <span class="brand__dot"></span>
      <span class="brand__name">VANTORA</span>
    </div>
  </div>
  <div class="front__rule"></div>

  <ul class="contact">
    <li>
      <svg viewBox="0 0 20 20" aria-hidden="true"><path d="M10 1a6 6 0 0 0-6 6c0 5 6 12 6 12s6-7 6-12a6 6 0 0 0-6-6zm0 8.5A2.5 2.5 0 1 1 10 4.5a2.5 2.5 0 0 1 0 5z" fill="var(--orange)"/></svg>
      address
    </li>
    <li>
      <svg viewBox="0 0 20 20" aria-hidden="true"><rect x="1" y="1" width="18" height="18" rx="4" fill="var(--orange)"/><path d="M6 5l2 0 1 3-1.5 1a7 7 0 0 0 3.5 3.5l1-1.5 3 1v2a1.5 1.5 0 0 1-1.5 1.5A9 9 0 0 1 4.5 6.5 1.5 1.5 0 0 1 6 5z" fill="#fff"/></svg>
      number
    </li>
    <li>
      <svg viewBox="0 0 20 20" aria-hidden="true"><circle cx="10" cy="10" r="9" fill="var(--orange)"/><rect x="5" y="6.5" width="10" height="7" rx="1" fill="none" stroke="#fff" stroke-width="1.4"/><path d="M5 7l5 4 5-4" fill="none" stroke="#fff" stroke-width="1.4"/></svg>
      email
    </li>
    <li>
      <svg viewBox="0 0 20 20" aria-hidden="true"><circle cx="10" cy="10" r="9" fill="var(--orange)"/><circle cx="10" cy="10" r="5.5" fill="none" stroke="#fff" stroke-width="1.3"/><path d="M4.5 10h11M10 4.5c-2.5 3-2.5 8 0 11M10 4.5c2.5 3 2.5 8 0 11" fill="none" stroke="#fff" stroke-width="1.1"/></svg>
      website
    </li>
  </ul>
</section>

</body>
</html>
```